Employee Benefits and Insurance Consulting

We are an existing company with over 30 years experience but are changing our name. We would like a simple design with grey tones.

Industry/Entity Type

Insurance

Contact Information for Business Card

Marlow Benefits Consulting
Gerald P Odell CEO
5172 Brackenfield Road
Louisville, TN 37777
gerald@marlowbx.com
865-412-3396 - O
865-247-5081 - C

```html
<!DOCTYPE html>
<html lang="en">
<head>
<meta charset="utf-8">
<title>Marlow Benefits Consulting – Business Cards</title>
<link rel="stylesheet" href="https://fonts.googleapis.com/css2?family=Open+Sans:wght@400;600&display=swap">
<style>
  :root {
    --teal: #20968b;
    --white: #ffffff;
    --black: #060606;
    --ink: #1e1e1e;
    --canvas: #e9e9e9;
  }
  * { margin: 0; padding: 0; box-sizing: border-box; }
  html, body { width: 1200px; height: 900px; overflow: hidden; }
  body {
    position: relative;
    background: var(--canvas);
    font-family: "Open Sans", Arial, sans-serif;
  }
  .card {
    position: absolute;
    border-radius: 16px;
    overflow: hidden;
  }
  .card--front { left: 78px; top: 35px; width: 588px; height: 362px; background: var(--white); }
  .card--back  { left: 389px; top: 505px; width: 566px; height: 350px; background: var(--black); }

  .band { position: absolute; left: 0; right: 0; background: var(--teal); }
  .card--front .band { top: 25px; height: 98px; }
  .card--back .band  { top: 32px; height: 96px; }

  .emblem-circle { position: absolute; border-radius: 50%; }
  .card--front .emblem-circle { left: 210px; top: -12px; width: 170px; height: 170px; background: var(--white); }
  .card--back .emblem-circle  { left: 198px; top: -5px; width: 170px; height: 170px; background: var(--black); }

  .company-name {
    position: absolute;
    left: 0; right: 0;
    text-align: center;
    color: var(--teal);
    font-weight: 600;
    font-size: 22px;
    letter-spacing: 1.5px;
    text-transform: uppercase;
  }
  .card--front .company-name { top: 134px; left: -10px; }
  .card--back .company-name  { top: 140px; left: -4px; }

  .person { position: absolute; left: 57px; top: 246px; width: 225px; text-align: right; }
  .person__name { color: var(--teal); font-weight: 600; font-size: 20px; text-align: left; white-space: nowrap; }
  .person__title { font-size: 15px; }
  .person__address { color: var(--ink); font-size: 15.5px; line-height: 22px; margin-top: 6px; }

  .contact-list { position: absolute; left: 348px; top: 251px; list-style: none; }
  .contact-list li {
    display: flex; align-items: center;
    height: 24.5px;
    color: var(--ink); font-size: 15.5px;
  }
  .contact-list svg { width: 13px; height: 13px; margin-right: 12px; fill: var(--teal); }

  .back-address {
    position: absolute; left: 0; right: 0; top: 291px;
    text-align: center; color: var(--white); font-size: 15px;
    word-spacing: 1px;
  }
</style>
</head>
<body>

<section class="card card--front" aria-label="Business card front">
  <div class="band"></div>
  <div class="emblem-circle"></div>
  <p class="company-name">Marlow Benefits Consulting</p>

  <div class="person">
    <p class="person__name">Gerald P Odell - <span class="person__title">CEO</span></p>
    <p class="person__address">5172 Brackenfield Road<br>Louisville, TN 37777</p>
  </div>

  <ul class="contact-list">
    <li>
      <svg viewBox="0 0 16 16" aria-hidden="true"><path d="M3.6 1.2l2.2 2.6-1.3 1.8c.9 2 2.6 3.7 4.6 4.6l1.8-1.3 2.6 2.2-1.2 2.4C7.6 13.4 2.6 8.4 1.2 3.6z"/></svg>
      865-247-5081
    </li>
    <li>
      <svg viewBox="0 0 16 16" aria-hidden="true"><path d="M4.5 0h7A1.5 1.5 0 0113 1.5v13a1.5 1.5 0 01-1.5 1.5h-7A1.5 1.5 0 013 14.5v-13A1.5 1.5 0 014.5 0zM5 2v10h6V2z"/></svg>
      865-412-3396
    </li>
    <li>
      <svg viewBox="0 0 16 16" aria-hidden="true"><path d="M1 3h14v10H1zM2.5 4.5v.4L8 8.6l5.5-3.7v-.4z"/></svg>
      gerald@marlowbx.com
    </li>
  </ul>
</section>

<section class="card card--back" aria-label="Business card back">
  <div class="band"></div>
  <div class="emblem-circle"></div>
  <p class="company-name">Marlow Benefits Consulting</p>
  <p class="back-address">5172 Brackenfield Road&nbsp; Louisville, TN 37777</p>
</section>

</body>
</html>
```